Postcard Design Project( QPRX 6.5in wide x 9in )

Painting Company
- Interior and Exterior Painting
- Wallpaper Removal and Installation
- Wood Staining
-Licensed and Insured HIC #KT739208
-website: www.kellermontpainting.com
-Facebook: @kmpainting
-Phone #: 555-318-2076
Fall Special Discount 10% off $500.00 or more
(QPRX Postcard size (6.5in wide x9)

People who are in need of painting

Painting

• Must be bold and make a statement. I need the people to hold on to the postcard and not throw it away.
• Should not look like you took it off a template.

```html
<!DOCTYPE html>
<html lang="en">
<head>
<meta charset="utf-8">
<title>Kellermont Painting Postcard</title>
<link href="https://fonts.googleapis.com/css2?family=Lato:ital,wght@0,300;0,400;0,700;0,900;1,900&display=swap" rel="stylesheet">
<style>
  :root {
    --backdrop: #231f20;
    --navy: #262a68;
    --red: #c1213a;
    --white: #ffffff;
    --grey-text: #4f4f55;
    --wall-light: #f7f5f1;
    --wall-mid: #e9e3d9;
    --wall-deep: #c9b89c;
    --room-top: #e6e8e9;
    --room-mid: #d5dde3;
    --room-floor: #eef0f0;
  }
  * { margin: 0; padding: 0; box-sizing: border-box; }
  html, body { width: 829px; height: 1200px; overflow: hidden; background: var(--backdrop); }
  body { position: relative; font-family: "Lato", Arial, sans-serif; }

  .card { position: absolute; left: 58px; width: 713px; height: 514px; overflow: hidden; white-space: nowrap; }
  .card--front { top: 71px; }
  .card--back { top: 613px; }

  .photo { position: absolute; inset: 0; }
  .card--front .photo {
    background: linear-gradient(105deg, var(--wall-light) 0%, var(--wall-light) 48%, var(--wall-mid) 66%, var(--wall-deep) 100%);
  }
  .card--back .photo {
    background: linear-gradient(170deg, var(--room-top) 0%, var(--room-mid) 50%, var(--room-floor) 100%);
  }

  .brand { position: absolute; left: 42px; display: flex; align-items: center; gap: 12px; }
  .card--front .brand { top: 32px; }
  .card--back .brand { top: 64px; }
  .brand__mark { width: 40px; height: 40px; background: var(--navy); }
  .brand__name { font-weight: 900; color: var(--navy); font-size: 31px; line-height: 33px; }

  .headline-top { position: absolute; left: 38px; top: 142px; font-size: 39.5px; font-weight: 900; color: var(--navy); letter-spacing: -0.3px; }
  .headline-main { position: absolute; left: 37px; top: 181px; font-size: 76px; font-weight: 900; color: var(--red); letter-spacing: -1.2px; line-height: 1; }

  .service-band {
    position: absolute; left: 0; top: 254px; width: 403px; height: 31px;
    background: var(--navy); border-radius: 0 16px 16px 0;
    color: var(--white); font-size: 16.8px; font-weight: 700; line-height: 31px; padding-left: 34px;
  }

  .promo-label { position: absolute; left: 34px; top: 297px; font-size: 22.8px; font-weight: 700; color: var(--navy); letter-spacing: -0.3px; }
  .promo-value { position: absolute; left: 32px; top: 320px; font-weight: 900; line-height: 1; }
  .promo-value__pct { font-size: 73px; color: var(--red); letter-spacing: -2px; }
  .promo-value__off { font-size: 58px; color: var(--navy); }
  .promo-min { position: absolute; left: 34px; top: 391px; font-weight: 900; color: var(--navy); font-size: 32px; }
  .promo-min__note { font-size: 25px; font-style: italic; color: var(--red); }

  .burst { position: absolute; left: 278px; top: 286px; width: 123px; height: 66px; }
  .burst svg { position: absolute; inset: 0; }
  .burst__text {
    position: absolute; inset: 0; display: flex; flex-direction: column; justify-content: center; align-items: center;
    color: var(--white); font-weight: 900; font-style: italic; font-size: 17px; line-height: 17px; transform: rotate(-5deg);
    padding-bottom: 8px;
  }

  .footer { position: absolute; left: 0; bottom: 0; width: 100%; height: 52px; }
  .footer__rule { position: absolute; left: 0; top: 0; width: 100%; height: 4px; background: var(--navy); }
  .footer__band {
    position: absolute; left: 0; top: 4px; width: 100%; height: 48px; background: var(--red);
    color: var(--white); font-size: 17px; font-weight: 700; text-align: center; line-height: 52px;
  }
  .license {
    position: absolute; left: 207px; bottom: 37px; width: 297px; height: 27px; border-radius: 14px;
    background: var(--navy); color: var(--white); font-size: 15.5px; font-weight: 700; text-align: center; line-height: 27px;
  }

  .stamp { position: absolute; left: 613px; top: 40px; width: 59px; height: 58px; background: #000; }

  .about-name { position: absolute; left: 43px; top: 181px; font-size: 52px; font-weight: 700; color: var(--red); letter-spacing: -0.3px; line-height: 1; }
  .about-sub { position: absolute; left: 43px; top: 244px; font-size: 33px; font-weight: 400; color: var(--navy); line-height: 1; }
  .about-text { position: absolute; left: 43px; top: 290px; width: 325px; font-size: 25.5px; font-weight: 300; color: var(--grey-text); line-height: 30.7px; white-space: normal; }

  .address-line { position: absolute; left: 425px; width: 247px; height: 1px; background: #222; }
  .address-line--1 { top: 326px; }
  .address-line--2 { top: 367px; }
  .address-line--3 { top: 407px; }
</style>
</head>
<body>

<section class="card card--front">
  <div class="photo" role="img" aria-label="Photo of a painter in white coveralls rolling paint onto a wall beside a wooden stepladder, with paint cans on a drop cloth"></div>

  <div class="brand">
    <span class="brand__mark"></span>
    <span class="brand__name">KELLERMONT<br>PAINTING</span>
  </div>

  <h1 class="headline-top">Interior and Exterior</h1>
  <div class="headline-main">PAINTING</div>

  <div class="service-band">WALLPAPER REMOVAL AND INSTALLATION</div>

  <div class="promo-label">Fall Special Discount</div>
  <div class="promo-value"><span class="promo-value__pct">10%</span> <span class="promo-value__off">off</span></div>
  <div class="promo-min">$500.00 <span class="promo-min__note">or more</span></div>

  <div class="burst">
    <svg viewBox="0 0 123 66" aria-hidden="true">
      <polygon fill="var(--red)" points="4,14 28,10 40,0 56,8 78,2 92,10 118,6 110,22 123,30 108,38 112,50 88,46 76,66 64,50 42,54 34,44 12,46 20,32 0,24 16,20"/>
    </svg>
    <div class="burst__text"><span>WOOD</span><span>STAINING</span></div>
  </div>

  <div class="footer">
    <div class="footer__rule"></div>
    <div class="footer__band">Fb: @kmpainting | web: www.kellermontpainting.com | Ph: 555-318-2076</div>
  </div>
  <div class="license">Licensed and Insured HIC #KT739208</div>
</section>

<section class="card card--back">
  <div class="photo" role="img" aria-label="Faded photo of an empty, freshly painted room with a ceiling fan and bright windows"></div>

  <div class="brand">
    <span class="brand__mark"></span>
    <span class="brand__name">KELLERMONT<br>PAINTING</span>
  </div>

  <div class="stamp"></div>

  <h2 class="about-name">KELLERMONT</h2>
  <div class="about-sub">PAINTING COMPANY</div>
  <p class="about-text">is a Veteran-owned business with experience of providing quality work for 10+ years in residential homes.</p>

  <div class="address-line address-line--1"></div>
  <div class="address-line address-line--2"></div>
  <div class="address-line address-line--3"></div>

  <div class="footer">
    <div class="footer__rule"></div>
    <div class="footer__band">Fb: @kmpainting | web: www.kellermontpainting.com | Ph: 555-318-2076</div>
  </div>
  <div class="license">Licensed and Insured HIC #KT739208</div>
</section>

</body>
</html>
```